Business Card Design Project

We need a business card design for a new company based in New York called "Quorra Mesh's". We do major installations of energy saving devices primarily LED lighting in large facilities. We would like a double sided card with our contact info on one side with our logo (to be designed) and on the other side the services we provide. We would like a heavy weight glossy card using the colors green and white. The final design should communicate environmental soundness and our market is very upscale corporations.
We would like our logo to illustrate LED lighting and we were thinking if we could get a stock picture of the Halvern Crest Building lit up on July 4th with red, white and blue LED lighting. The alternative would be anything that connotes environmentally proper thinking. It could be either a picture or a design.

```html
<!DOCTYPE html>
<html lang="en">
<head>
<meta charset="utf-8">
<title>Quorra Mesh's – Business Card</title>
<link rel="stylesheet" href="https://fonts.googleapis.com/css2?family=Open+Sans:ital,wght@0,400;0,600;0,700;1,400&display=swap">
<style>
  :root {
    --page-bg: #ecebe8;
    --card-white: #ffffff;
    --card-grey: #e4e4e4;
    --green-light: #9bd43c;
    --green-mid: #5cbc22;
    --green-deep: #14980a;
    --green-text: #6cbf2a;
    --green-url: #1f8a12;
    --ink: #333333;
    --ink-soft: #555555;
    --white: #ffffff;
  }
  * { box-sizing: border-box; margin: 0; padding: 0; }
  html, body { width: 1200px; height: 868px; overflow: hidden; }
  body {
    background: var(--page-bg);
    font-family: "Open Sans", Arial, sans-serif;
    position: relative;
  }
  .card {
    position: absolute;
    width: 540px;
    height: 310px;
    border-radius: 14px;
    overflow: hidden;
    box-shadow: 0 10px 28px rgba(0,0,0,.18);
  }

  /* Front side */
  .card-front {
    left: 60px; top: 120px;
    background: linear-gradient(180deg, var(--card-white) 0%, var(--card-white) 62%, var(--card-grey) 100%);
  }
  .front-brand {
    position: absolute;
    left: 44px; top: 196px;
    font-size: 30px;
    font-weight: 400;
    color: var(--green-text);
    letter-spacing: .2px;
  }
  .holder {
    position: absolute;
    right: 64px; top: 56px;
    text-align: right;
  }
  .holder-name { font-size: 20px; color: var(--green-text); font-weight: 400; }
  .holder-role { font-size: 11px; color: var(--ink); margin-top: -2px; }
  .contact {
    position: absolute;
    right: 44px; top: 132px;
    list-style: none;
    text-align: right;
  }
  .contact li {
    display: flex; justify-content: flex-end; align-items: center; gap: 8px;
    font-size: 11px; line-height: 16px;
    color: var(--ink-soft);
    font-style: italic;
  }
  .contact li.is-link { color: var(--green-url); font-style: normal; font-weight: 600; }
  .contact svg { width: 9px; height: 9px; flex: none; }
  .contact .spacer { width: 9px; }

  /* Back side */
  .card-back {
    left: 600px; top: 440px;
    background: var(--card-white);
  }
  .back-field {
    position: absolute; inset: 0 0 42px 0;
    background: linear-gradient(160deg, var(--green-light) 0%, var(--green-mid) 50%, var(--green-deep) 100%);
  }
  .back-brand {
    position: absolute;
    left: 250px; top: 36px;
    font-size: 30px;
    font-weight: 400;
    color: var(--white);
  }
  .services {
    position: absolute;
    top: 104px; left: 206px;
    display: grid;
    grid-template-columns: 176px 150px;
    grid-auto-flow: column;
    grid-template-rows: repeat(6, 24px);
    list-style: none;
  }
  .services li {
    display: flex; align-items: center; gap: 9px;
    font-size: 15px; font-weight: 600; color: var(--white);
  }
  .tick { width: 14px; height: 14px; flex: none; }
  .back-url {
    position: absolute; left: 0; right: 0; bottom: 8px;
    text-align: center;
    font-size: 19px; font-weight: 700;
    color: var(--green-url);
  }
</style>
</head>
<body>

  <section class="card card-front" aria-label="Card front">
    <div class="front-brand">Quorra Mesh's</div>

    <div class="holder">
      <div class="holder-name">Dana Rell</div>
      <div class="holder-role">CEO</div>
    </div>

    <ul class="contact">
      <li>Address line 1
        <svg viewBox="0 0 10 10"><path d="M5 0a3.3 3.3 0 0 0-3.3 3.3C1.7 6 5 10 5 10s3.3-4 3.3-6.7A3.3 3.3 0 0 0 5 0zm0 4.6a1.3 1.3 0 1 1 0-2.6 1.3 1.3 0 0 1 0 2.6z" fill="#444"/></svg>
      </li>
      <li>Address line 2 <span class="spacer"></span></li>
      <li>+380 00 000 000
        <svg viewBox="0 0 10 10"><path d="M2 0.5l2 2-1 1.2c.6 1.3 1.6 2.3 2.9 2.9l1.2-1 2 2-1.3 1.7C4.5 9 1 5.5.3 1.8z" fill="#444"/></svg>
      </li>
      <li>+380 00 000 000
        <svg viewBox="0 0 10 10"><rect x="2.5" y="0.5" width="5" height="9" rx="1" fill="none" stroke="#444" stroke-width="1.1"/><circle cx="5" cy="8" r=".6" fill="#444"/></svg>
      </li>
      <li class="is-link">dana.rell@quorramesh.com
        <svg viewBox="0 0 10 10"><rect x=".5" y="2" width="9" height="6" fill="#444"/><path d="M.5 2L5 5.6 9.5 2" fill="none" stroke="#fff" stroke-width=".9"/></svg>
      </li>
      <li class="is-link">www.quorramesh.com
        <svg viewBox="0 0 10 10"><circle cx="5" cy="5" r="4.4" fill="none" stroke="#444" stroke-width="1.1"/><ellipse cx="5" cy="5" rx="1.8" ry="4.4" fill="none" stroke="#444" stroke-width=".8"/><path d="M.6 5h8.8" stroke="#444" stroke-width=".8"/></svg>
      </li>
    </ul>
  </section>

  <section class="card card-back" aria-label="Card back">
    <div class="back-field"></div>
    <div class="back-brand">Quorra Mesh's</div>

    <ul class="services">
      <li><svg class="tick" viewBox="0 0 14 14"><rect width="14" height="14" rx="2" fill="#fff"/><path d="M3 7.2l2.7 2.7L11 4" fill="none" stroke="#2a9a12" stroke-width="2.2"/></svg>Servce line 1</li>
      <li><svg class="tick" viewBox="0 0 14 14"><rect width="14" height="14" rx="2" fill="#fff"/><path d="M3 7.2l2.7 2.7L11 4" fill="none" stroke="#2a9a12" stroke-width="2.2"/></svg>Servce line 2</li>
      <li><svg class="tick" viewBox="0 0 14 14"><rect width="14" height="14" rx="2" fill="#fff"/><path d="M3 7.2l2.7 2.7L11 4" fill="none" stroke="#2a9a12" stroke-width="2.2"/></svg>Servce line 3</li>
      <li><svg class="tick" viewBox="0 0 14 14"><rect width="14" height="14" rx="2" fill="#fff"/><path d="M3 7.2l2.7 2.7L11 4" fill="none" stroke="#2a9a12" stroke-width="2.2"/></svg>Servce line 4</li>
      <li><svg class="tick" viewBox="0 0 14 14"><rect width="14" height="14" rx="2" fill="#fff"/><path d="M3 7.2l2.7 2.7L11 4" fill="none" stroke="#2a9a12" stroke-width="2.2"/></svg>Servce line 5</li>
      <li><svg class="tick" viewBox="0 0 14 14"><rect width="14" height="14" rx="2" fill="#fff"/><path d="M3 7.2l2.7 2.7L11 4" fill="none" stroke="#2a9a12" stroke-width="2.2"/></svg>Servce line 6</li>
      <li><svg class="tick" viewBox="0 0 14 14"><rect width="14" height="14" rx="2" fill="#fff"/><path d="M3 7.2l2.7 2.7L11 4" fill="none" stroke="#2a9a12" stroke-width="2.2"/></svg>Servce line 7</li>
      <li><svg class="tick" viewBox="0 0 14 14"><rect width="14" height="14" rx="2" fill="#fff"/><path d="M3 7.2l2.7 2.7L11 4" fill="none" stroke="#2a9a12" stroke-width="2.2"/></svg>Servce line 8</li>
      <li><svg class="tick" viewBox="0 0 14 14"><rect width="14" height="14" rx="2" fill="#fff"/><path d="M3 7.2l2.7 2.7L11 4" fill="none" stroke="#2a9a12" stroke-width="2.2"/></svg>Servce line 9</li>
      <li><svg class="tick" viewBox="0 0 14 14"><rect width="14" height="14" rx="2" fill="#fff"/><path d="M3 7.2l2.7 2.7L11 4" fill="none" stroke="#2a9a12" stroke-width="2.2"/></svg>Servce line 10</li>
      <li><svg class="tick" viewBox="0 0 14 14"><rect width="14" height="14" rx="2" fill="#fff"/><path d="M3 7.2l2.7 2.7L11 4" fill="none" stroke="#2a9a12" stroke-width="2.2"/></svg>Servce line 11</li>
      <li><svg class="tick" viewBox="0 0 14 14"><rect width="14" height="14" rx="2" fill="#fff"/><path d="M3 7.2l2.7 2.7L11 4" fill="none" stroke="#2a9a12" stroke-width="2.2"/></svg>Servce line 12</li>
    </ul>

    <div class="back-url">www.quorramesh.com</div>
  </section>

</body>
</html>
```